Valtora

Standard Business Card design.
Sample two-sided design uploaded. White front, Black back.
Would like white shield to be on all black background side.
Willing to look at a couple creative designs, but nothing crazy.
Preference for a classic, confident, strong design.

```html
<!DOCTYPE html>
<html lang="en">
<head>
<meta charset="utf-8">
<title>Valtora – Business Card</title>
<link rel="stylesheet" href="https://fonts.googleapis.com/css2?family=Fira+Sans+Condensed:wght@300;400;500;600&display=swap">
<style>
  :root {
    --ink: #000000;
    --paper: #ffffff;
    --edge: #d0d0d0;
    --rule: #bdbdbd;
  }
  * { margin: 0; padding: 0; box-sizing: border-box; }
  html, body {
    width: 1200px;
    height: 684px;
    overflow: hidden;
    background: var(--paper);
  }
  .canvas {
    position: relative;
    width: 1200px;
    height: 684px;
    font-family: "Fira Sans Condensed", sans-serif;
  }
  .card-back {
    position: absolute;
    left: 108px;
    top: 165px;
    width: 466px;
    height: 302px;
    background: var(--ink);
    display: flex;
    align-items: center;
    justify-content: center;
  }
  .card-back .brand-name {
    color: var(--paper);
    font-size: 64px;
    font-weight: 600;
    letter-spacing: 8px;
    text-transform: uppercase;
  }
  .card-front {
    position: absolute;
    left: 592px;
    top: 166px;
    width: 466px;
    height: 302px;
    background: var(--paper);
    border: 1px solid var(--edge);
  }
  .card-front .brand-name {
    position: absolute;
    left: 80px;
    width: 174px;
    top: 136px;
    text-align: center;
    color: var(--ink);
    font-size: 28px;
    font-weight: 600;
    letter-spacing: 4px;
    text-transform: uppercase;
  }
  .contact-panel {
    position: absolute;
    left: 254px;
    top: -1px;
    width: 212px;
    height: 302px;
    background: var(--ink);
    color: var(--paper);
    text-align: right;
  }
  .person-name {
    position: absolute;
    right: 32px;
    top: 138px;
    font-size: 18px;
    font-weight: 600;
    white-space: nowrap;
  }
  .person-role {
    position: absolute;
    right: 32px;
    top: 159px;
    font-size: 17px;
    font-weight: 400;
    white-space: nowrap;
  }
  .panel-rule {
    position: absolute;
    left: 0;
    right: 32px;
    top: 183px;
    height: 1px;
    background: var(--rule);
  }
  .contact-list {
    position: absolute;
    right: 32px;
    top: 228px;
    list-style: none;
    font-size: 15px;
    line-height: 19px;
    font-weight: 300;
    white-space: nowrap;
  }
  .contact-list .web { font-weight: 600; font-size: 14px; }
</style>
</head>
<body>
<main class="canvas">
  <section class="card-back">
    <span class="brand-name">Valtora</span>
  </section>

  <section class="card-front">
    <span class="brand-name">Valtora</span>
    <div class="contact-panel">
      <p class="person-name">Name Surname</p>
      <p class="person-role">Executive Director</p>
      <div class="panel-rule"></div>
      <ul class="contact-list">
        <li>hello@valtora.com</li>
        <li>T. 1234 567 7890</li>
        <li class="web">www.valtora.com</li>
      </ul>
    </div>
  </section>
</main>
</body>
</html>
```